Design eBook Cover for Homeowner Association (HOA) book

We need a cover design for an eBook entitled "The Residents Council Leader's Manual: Practical Steps and Proven Methods".

Title: The Residents Council Leader's Manual

Subtitle: Practical Steps and Proven Methods

Name of Author: Gerald Whitcombe, CMA

Style: Professional Guide

Testimonial: "This book is an indispensable tool for anyone on an HOA board. The expert advice and practical approach in 'The Residents Council Leader's Manual' have made a world of difference in our community. Every board member should have a copy!"
— Marla Quint, HOA Board President

I have uploaded a file as design inspiration but not locked into the colors or look. Just want a clean, professional looking cover.

Target Market(s)

Board members of HOAs (Homeowners associations) in the United States

Industry/Entity Type

Real Estate, HOA

Requirements
Must have
• Clean, professional appearance that conveys authority

```html
<!DOCTYPE html>
<html lang="en">
<head>
<meta charset="utf-8">
<title>The Residents Council Leader's Manual — Cover</title>
<link href="https://fonts.googleapis.com/css2?family=Oswald:wght@600;700&family=Cinzel:wght@600&family=Montserrat:wght@500&display=swap" rel="stylesheet">
<style>
  :root {
    --backdrop: #e9e9e8;
    --cover-black: #050507;
    --ink-white: #ffffff;
    --accent-gold: #c9923f;
    --author-ink: #0b0b0b;
    --board-light: #b9bcc0;
    --board-dark: #1a1b1d;
  }
  html, body {
    margin: 0;
    padding: 0;
    width: 1200px;
    height: 1159px;
    overflow: hidden;
    background: var(--backdrop);
  }
  .cover {
    position: absolute;
    left: 287px;
    top: 109px;
    width: 627px;
    height: 941px;
    background: var(--cover-black);
    overflow: hidden;
  }
  .cover-title {
    position: absolute;
    left: 0;
    top: 0;
    width: 627px;
    height: 470px;
  }
  .cover-title text {
    font-family: "Oswald", "Arial Narrow", sans-serif;
    font-weight: 700;
    fill: var(--ink-white);
  }
  .cover-title .title-lead { font-weight: 600; }
  .cover-title .title-accent { fill: var(--accent-gold); }
  .cover-title .title-rule { fill: var(--ink-white); }
  .cover-subtitle {
    position: absolute;
    left: 67px;
    width: 499px;
    top: 478px;
    margin: 0;
    font-family: "Cinzel", "Times New Roman", serif;
    font-weight: 600;
    font-size: 20px;
    letter-spacing: 0.8px;
    color: var(--ink-white);
    text-align: center;
    white-space: nowrap;
  }
  .cover-visual {
    position: absolute;
    left: 0;
    top: 515px;
    width: 627px;
    height: 355px;
    background:
      radial-gradient(ellipse 28% 40% at 44% 72%, rgba(201,146,63,0.85), rgba(201,146,63,0) 70%),
      radial-gradient(ellipse 60% 45% at 55% 55%, rgba(200,202,206,0.55), rgba(200,202,206,0) 75%),
      linear-gradient(180deg, var(--cover-black) 0%, #2a2b2e 45%, var(--board-light) 78%, var(--board-dark) 100%);
  }
  .author-band {
    position: absolute;
    left: 0;
    top: 870px;
    width: 627px;
    height: 71px;
    background: var(--accent-gold);
    display: flex;
    align-items: center;
    justify-content: center;
  }
  .author-name {
    margin: 0;
    font-family: "Montserrat", "Helvetica", sans-serif;
    font-weight: 500;
    font-size: 35px;
    letter-spacing: 0.5px;
    color: var(--author-ink);
    white-space: nowrap;
  }
</style>
</head>
<body>
  <main class="cover">
    <svg class="cover-title" viewBox="0 0 627 470" aria-label="The Residents Council Leader's Manual">
      <rect class="title-rule" x="69" y="80" width="181" height="7"/>
      <rect class="title-rule" x="393" y="80" width="166" height="7"/>
      <text class="title-lead" x="259" y="88" font-size="56" textLength="124" lengthAdjust="spacingAndGlyphs">THE</text>
      <text class="title-accent" x="67" y="181" font-size="94" textLength="493" lengthAdjust="spacingAndGlyphs">RESIDENTS</text>
      <text x="67" y="272" font-size="94" textLength="493" lengthAdjust="spacingAndGlyphs">COUNCIL</text>
      <text x="67" y="363" font-size="94" textLength="493" lengthAdjust="spacingAndGlyphs">LEADER'S</text>
      <text x="67" y="454" font-size="94" textLength="493" lengthAdjust="spacingAndGlyphs">MANUAL</text>
    </svg>
    <p class="cover-subtitle">PRACTICAL STEPS AND PROVEN METHODS</p>
    <div class="cover-visual" role="img" aria-label="Photograph of a gold chess pawn standing in front of a row of blurred silver pawns on a reflective chessboard"></div>
    <footer class="author-band">
      <p class="author-name">GERALD WHITCOMBE, CMA</p>
    </footer>
  </main>
</body>
</html>
```